Landing Page that will convert (Design Only Landing Page Project)

I am looking for a design that will resonate with a dentist, doctor or anyone business owner in the medical field. My goal is to have then scheduled a 15 min session with me at the end to discuss how I can help then meet there financial goals (short or long term)

I am open to all design concepts and suggestions as far as the important contents or links that should be on the page (ie. Main menu like, Home, About, Services, Schedule, Contact Us).

There is no right or wrong answer, just need a great accounting/financing landing page. Again the project is for just the design of the page, and coding will be done elsewhere.

Target Market(s)

medical professionals, this includes small business owners of privately held office suck as medical doctors, dentist, ophthalmologist, chiropractors, etc

Industry/Entity Type

Finance And Accounting

Colors
fdfdfd
1b1b1b
f3f1f8
e4daeb

Requirements
Must have
• The goal of this landing page is to have the visitor schedule a 15min discovery call, therefore, a calender scheduling option is ideal, so we can understand their goals and see what obstacles they are facing and therefore avoid those obstacles before they become a burden
Nice to have
• A video background or maybe a medical professional office in that way they feel connected. For design purposes just use a video/image placeholder. I feel more is less if we can research some of the most successful landing page design and incorporate some of those elements that would to great.
• I saw this example and thought it was ok
• https://www.plovarte.com/#features
• WHAT I LIKE ABOUT THIS DESIGN:
• - It's simple, clean,
• - font is readable,
• - like the illustration
• - elegance
• - It clearly defines what the use should do, its intuitive, walks the user to the bottom of the page and give them the option of whether to signup or exit the page.

```html
<!DOCTYPE html>
<html lang="en">
<head>
<meta charset="utf-8">
<title>Ledgerwell – Finance Management</title>
<link href="https://fonts.googleapis.com/css2?family=Montserrat:wght@300;500;600;700&display=swap" rel="stylesheet">
<style>
  :root{
    --bg:#fcfafd;
    --ink:#1b1b1b;
    --plum:#4b3660;
    --plum-dark:#3d2752;
    --lilac:#9b7bb5;
    --lilac-soft:#e4daeb;
    --mist:#f3f1f8;
    --pink:#cd6aa8;
    --pink-faint:#f5e3ee;
    --text:#555;
    --white:#ffffff;
  }
  *{margin:0;padding:0;box-sizing:border-box}
  html,body{width:1200px;height:1018px;overflow:hidden;background:var(--bg)}
  body{position:relative;font-family:Arial,Helvetica,sans-serif;color:var(--text)}
  .hero-visual{position:absolute;left:0;top:0;width:1200px;height:520px}
  .side-glow{position:absolute;left:-60px;top:575px;width:320px;height:360px;border-radius:50%;
    background:radial-gradient(closest-side,var(--pink-faint),rgba(245,227,238,0))}
  .header{position:absolute;left:132px;top:18px;width:936px;height:44px;display:flex;align-items:center}
  .brand{display:flex;align-items:center;gap:8px;font-family:Montserrat,sans-serif;font-weight:300;font-size:23px;color:var(--plum);letter-spacing:.2px}
  .brand-mark{width:10px;height:10px;border:1.5px solid var(--plum);border-radius:50%}
  .nav{margin-left:auto;display:flex;align-items:center;gap:31px;font-size:11.5px;font-weight:700;letter-spacing:.2px}
  .nav a{text-decoration:none;color:var(--lilac)}
  .nav a.is-active{color:var(--plum)}
  .nav .cta{background:var(--lilac);color:var(--white);padding:12px 12px;border-radius:2px;margin-left:-1px}
  .hero-copy{position:absolute;left:131px;top:182px;width:400px}
  .hero-title{font-family:Montserrat,sans-serif;font-size:32px;line-height:41px;font-weight:700;color:var(--plum)}
  .hero-title span{display:block;font-weight:300;color:var(--lilac)}
  .hero-text{margin-top:16px;font-size:12.8px;line-height:21px;color:var(--text);width:372px}
  .hero-actions{margin-top:24px;display:flex;gap:18px}
  .btn{display:inline-flex;align-items:center;justify-content:center;height:37px;font-size:11.5px;font-weight:700;text-decoration:none;border-radius:2px}
  .btn-primary{width:123px;background:var(--lilac);color:var(--white);box-shadow:0 8px 14px rgba(155,123,181,.3)}
  .btn-outline{width:123px;border:1px solid #b9b2c2;color:var(--plum);background:var(--white)}
  .features{position:absolute;left:0;top:612px;width:1200px;text-align:center}
  .features-title{font-family:Montserrat,sans-serif;font-size:32px;font-weight:700;color:var(--plum)}
  .features-intro{margin:22px auto 0;width:560px;font-size:12.8px;line-height:21px}
  .feature-list{position:absolute;left:133px;top:146px;width:935px;height:211px}
  .feature-card{position:absolute;top:0;width:203px;height:211px;background:var(--white);border-radius:4px;box-shadow:0 10px 30px rgba(75,54,96,.07);display:flex;flex-direction:column;align-items:center}
  .feature-card svg{margin-top:30px}
  .feature-name{margin-top:14px;font-family:Montserrat,sans-serif;font-weight:500;font-size:17px;line-height:22px;color:var(--plum)}
</style>
</head>
<body>

<svg class="hero-visual" viewBox="0 0 1200 520">
  <defs>
    <linearGradient id="photoTone" x1="0" y1="0" x2="1" y2="1">
      <stop offset="0" stop-color="#f4f2f7"/>
      <stop offset=".4" stop-color="#e3dfec"/>
      <stop offset=".7" stop-color="#c9c3d8"/>
      <stop offset="1" stop-color="#7f84bd"/>
    </linearGradient>
  </defs>
  <path role="img" aria-label="Photo: doctor in a white coat at a desk working a calculator with a pen" fill="url(#photoTone)"
        d="M528 0 H1200 V360 L1070 486 Q1040 518 1000 514 L616 378 Z"/>
</svg>

<div class="side-glow" role="img" aria-label="Soft pink background accent"></div>

<header class="header">
  <div class="brand"><span class="brand-mark"></span>Ledgerwell</div>
  <nav class="nav">
    <a class="is-active" href="#">HOME</a>
    <a href="#">ABOUT</a>
    <a href="#">SERVICES</a>
    <a href="#">SCHEDULE</a>
    <a href="#">CONTACT US</a>
    <a class="cta" href="#">SCHEDULED A SESSION</a>
  </nav>
</header>

<section class="hero-copy">
  <h1 class="hero-title">Finance Management<span>is heart of any business</span></h1>
  <p class="hero-text">Lorem ipsum dolor sit amet, consectetur adipiscing elit. Nullam in auctor urna.</p>
  <div class="hero-actions">
    <a class="btn btn-primary" href="#">LEARN MORE</a>
    <a class="btn btn-outline" href="#">VIEW SERVICES</a>
  </div>
</section>

<section class="features">
  <h2 class="features-title">Some of the Key Features</h2>
  <p class="features-intro">Lorem ipsum dolor sit amet, consectetur adipiscing elit. Nullam in auctor urna. Maecenas tempus lorem felis, vel mattis nisl viverra sit amet.</p>
  <div class="feature-list">
    <article class="feature-card" style="left:0">
      <svg width="84" height="94" viewBox="0 0 84 94">
        <polygon points="42,4 80,25 80,69 42,90 4,69 4,25" fill="#9b7bb5" stroke="#9b7bb5" stroke-width="8" stroke-linejoin="round"/>
        <g fill="none" stroke="#fff" stroke-width="1.6">
          <circle cx="42" cy="47" r="16"/>
          <ellipse cx="42" cy="47" rx="7" ry="16"/>
          <line x1="26" y1="47" x2="58" y2="47"/>
          <line x1="29" y1="39" x2="55" y2="39"/>
          <line x1="29" y1="55" x2="55" y2="55"/>
          <circle cx="42" cy="26" r="2.5"/><circle cx="42" cy="68" r="2.5"/>
          <circle cx="22" cy="36" r="2.5"/><circle cx="62" cy="36" r="2.5"/>
          <circle cx="22" cy="58" r="2.5"/><circle cx="62" cy="58" r="2.5"/>
        </g>
      </svg>
      <h3 class="feature-name">Expand<br>Your Reach</h3>
    </article>
    <article class="feature-card" style="left:245px">
      <svg width="84" height="94" viewBox="0 0 84 94">
        <polygon points="42,4 80,25 80,69 42,90 4,69 4,25" fill="#3d2752" stroke="#3d2752" stroke-width="8" stroke-linejoin="round"/>
        <g fill="none" stroke="#fff" stroke-width="1.6">
          <rect x="26" y="58" width="5" height="7"/><rect x="34" y="54" width="5" height="11"/>
          <rect x="42" y="50" width="5" height="15"/><rect x="50" y="44" width="5" height="21"/>
          <line x1="22" y1="67" x2="62" y2="67"/>
          <path d="M24 56 Q44 50 60 31 M55 31 H60 V36"/>
          <line x1="26" y1="33" x2="34" y2="33"/><line x1="26" y1="37" x2="33" y2="37"/><line x1="26" y1="41" x2="32" y2="41"/>
        </g>
      </svg>
      <h3 class="feature-name">Higher Annualized<br>Growth Rate</h3>
    </article>
    <article class="feature-card" style="left:487px">
      <svg width="84" height="94" viewBox="0 0 84 94">
        <polygon points="42,4 80,25 80,69 42,90 4,69 4,25" fill="#cd6aa8" stroke="#cd6aa8" stroke-width="8" stroke-linejoin="round"/>
        <g fill="none" stroke="#fff" stroke-width="1.6">
          <rect x="24" y="31" width="30" height="36" rx="2"/>
          <circle cx="39" cy="30" r="5"/><path d="M39 27.5v5M36.5 30h5"/>
          <path d="M28 42l2 2 3-3M28 50l2 2 3-3M28 58l2 2 3-3"/>
          <line x1="36" y1="43" x2="50" y2="43"/><line x1="36" y1="51" x2="50" y2="51"/><line x1="36" y1="59" x2="50" y2="59"/>
          <path d="M57 36h5v26l-2.5 5-2.5-5z"/>
        </g>
      </svg>
      <h3 class="feature-name">Manage<br>Your Patients</h3>
    </article>
    <article class="feature-card" style="left:732px">
      <svg width="84" height="94" viewBox="0 0 84 94">
        <polygon points="42,4 80,25 80,69 42,90 4,69 4,25" fill="#4b3660" stroke="#4b3660" stroke-width="8" stroke-linejoin="round"/>
        <g fill="none" stroke="#fff" stroke-width="1.6">
          <circle cx="42" cy="50" r="17"/><circle cx="42" cy="50" r="13"/>
          <rect x="37" y="26" width="10" height="4"/><line x1="42" y1="30" x2="42" y2="33"/>
          <line x1="27" y1="34" x2="31" y2="38"/><line x1="57" y1="34" x2="53" y2="38"/>
          <path d="M42 41v9"/><circle cx="42" cy="50" r="1.5"/>
        </g>
      </svg>
      <h3 class="feature-name">Track<br>Your Time</h3>
    </article>
  </div>
</section>

</body>
</html>
```